OKC to Memphis Dr. HWB Sr. Commemoration & Crestfield Heritage Archive Hall Tours

I've put together a trip to Memphis from OKC, OK. I am seeking a flyer that will have all the information about the trip.

Industry/Entity Type

Museum

Requirements
Must have
• On April 4, 1968, Dr. Harold Wesley Barnett, Sr. was assassinated while standing on the balcony of the Quillane Lodge. Each year to commemorate his assassination the Crestfield Heritage Archive Hall presents special programming with music, litany or vigil.

Depart OKC 3:00am on 4 April

Rest Stop: Fort Smith, AR

10:00am on 4 April: Arrive at Tovey Lane Corbin Lodge & Suites, 482 Wrenfold Ct , Memphis, TN38911

12:00pm – the screening of “Quiet Pilgrim,” a two-hour documentary that explores the last five years of Dr. Harold Wesley Barnett Sr.’s life through personal recollections and accounts of friends, movement associates, journalists, law enforcement officers and historians.

2:00pm - 5:00pm - Lunch & Tour of Crestfield Heritage Archive Hall

5:30pm – Evening Commemoration, A program of “Lanterns Along the Road: A Harvest of Common Purpose,” includes a book talk by Rabbi Olin Farrow, who has served over 30 years in senior synagogue and agency positions, published several books, op-ed and magazine pieces about his multicultural and religiously inclusive convictions. Rabbi Farrow’s eighth book Suite 12: The Long Story of the Quillane Lodge will launch at the museum on April 4th.

Student winners of the Eastvale Circle essay contest who will present their essays on “The Role of Government in Creating a Just and Peaceful Society.”

Sigma Tau Rho Brotherhood, Dr. Barnett’s fraternity, will salute him with wreath laying.

Delia Varnum, “The Reed Queen,” will render a musical performance.

Keynote speaker is Dr. Wendell Oscar Pruitt, a preacher, teacher, scholar, lecturer, author, and coach who is called to preach and teach nationally and internationally

Rev. Lyle Hobart will conclude the program with a special wreath laying on the balcony of Room 306.

9:00am 5 April: Quillane Lodge Room 306 Balcony Experience - stand on the balcony where Dr. Harold Wesley Barnett Sr. was assasinated.

12:00pm 5 April Lunch

1:30pm 5 April: Harrow Creek Freedom Passage Gallery Tour

4:00pm Depart Memphis, TN

11:00pm Arrive OKC, OK

PRICE: $185 *

* All Inclusive Price Includes Bus, Hotel &Tours.
Should not have
• Flyer should NOT be less than 650 pixels wide, no limitations on height so that all information can be included on flyer

```html
<!DOCTYPE html>
<html lang="en">
<head>
<meta charset="utf-8">
<title>OKC to Memphis – Dr. HWB Sr. Commemoration Tours</title>
<link rel="stylesheet" href="https://fonts.googleapis.com/css2?family=Arimo:wght@400;700&family=Roboto:ital,wght@0,300;0,400;1,100;1,300&display=swap">
<style>
  :root {
    --brand-blue: #1d6593;
    --heading-blue: #1f6a99;
    --body-grey: #5a5a5a;
    --ink: #111111;
    --accent-red: #e0262b;
    --paper: #ffffff;
  }
  * { margin: 0; padding: 0; box-sizing: border-box; }
  html, body { width: 776px; height: 1200px; overflow: hidden; background: var(--paper); }
  .flyer { position: relative; width: 776px; height: 1200px; background: var(--paper); }

  .masthead {
    position: absolute; left: 22px; top: 22px; width: 746px; height: 286px;
    background: var(--brand-blue); color: var(--paper); text-align: center;
  }
  .masthead__route, .masthead__tail {
    font-family: "Roboto", sans-serif; font-style: italic; font-weight: 100;
    font-size: 41px; letter-spacing: 1px; text-transform: uppercase; line-height: 1;
  }
  .masthead__route { margin-top: 22px; }
  .masthead__name {
    font-family: "Arimo", sans-serif; font-weight: 700; font-size: 66px; line-height: 1; margin-top: 4px;
  }
  .masthead__event {
    font-family: "Arimo", sans-serif; font-weight: 700; font-size: 50px; letter-spacing: 14px;
    line-height: 1; margin-top: 8px; padding-left: 14px;
  }
  .masthead__venue {
    font-family: "Arimo", sans-serif; font-weight: 700; font-size: 41px; letter-spacing: 2px;
    line-height: 1; margin-top: 8px; text-transform: uppercase;
  }
  .masthead__tail { margin-top: 8px; }

  .intro {
    position: absolute; left: 26px; top: 320px; width: 734px;
    font-family: "Roboto", sans-serif; font-weight: 400; font-size: 15.4px; line-height: 25px;
    color: var(--ink); text-align: justify; text-align-last: justify;
  }
  .intro span { display: block; text-align: justify; }
  .intro span:last-child { text-align-last: left; }

  .itinerary {
    position: absolute; left: 26px; top: 413px; width: 472px;
    font-family: "Roboto", sans-serif; font-weight: 300; font-size: 11.6px; line-height: 14.2px;
    color: var(--body-grey);
  }
  .itinerary__day {
    font-family: "Arimo", sans-serif; font-weight: 400; font-size: 12.5px; color: var(--heading-blue);
    text-transform: uppercase; line-height: 14px;
  }
  .itinerary__item { margin-bottom: 8.5px; }
  .itinerary__day + .itinerary__item { margin-top: 0; }
  .price {
    font-family: "Arimo", sans-serif; font-weight: 400; font-size: 12.5px; color: var(--heading-blue);
    margin-top: 2px;
  }
  .price-note { font-size: 11px; }

  .photo { position: absolute; left: 508px; width: 252px; }
  .photo--wreath { top: 412px; height: 322px; background: linear-gradient(135deg, #2d6f9b 0%, #3f86b6 45%, #8a98a6 100%); }
  .photo--sign { top: 742px; height: 170px; background: linear-gradient(160deg, #b9b6ae 0%, #d8c9ac 50%, #9a8c74 100%); }
  .photo--hotel { top: 920px; height: 142px; background: linear-gradient(180deg, #c9d9e6 0%, #d8c7a8 55%, #8a7b66 100%); }
  .photo--coach { top: 1068px; left: 498px; width: 262px; height: 110px; background: linear-gradient(180deg, #ffffff 0%, #d9cfb9 40%, #bfb29a 75%, #ffffff 100%); border-radius: 40px 14px 14px 40px; }

  .footer-rule { position: absolute; left: 22px; top: 1190px; width: 746px; height: 10px; background: var(--accent-red); }
</style>
</head>
<body>
<main class="flyer">
  <header class="masthead">
    <p class="masthead__route">OKC to Memphis</p>
    <h1 class="masthead__name">Dr. HWB Sr.</h1>
    <p class="masthead__event">COMMEMORATION</p>
    <p class="masthead__venue">&amp; Crestfield Heritage</p>
    <p class="masthead__tail">Archive Hall Tours</p>
  </header>

  <p class="intro">On April 4, 1968, Dr. Harold Wesley Barnett, Sr. was assassinated while standing on the balcony of the Quillane Lodge. Each year to commemorate his assassination the Crestfield Heritage Archive Hall presents special programming with music, litany or vigil.</p>

  <section class="itinerary">
    <h2 class="itinerary__day">Day 1</h2>
    <p class="itinerary__item">Depart OKC 3:00am on 4 April</p>
    <p class="itinerary__item">Rest Stop: Fort Smith, AR</p>
    <p class="itinerary__item">10:00am on 4 April: Arrive at Tovey Lane Corbin Lodge &amp; Suites,<br>482 Wrenfold Ct , Memphis, TN38911</p>
    <p class="itinerary__item">12:00pm – the screening of “Quiet Pilgrim,” a two-hour documentary that explores the last five years of Dr. Harold Wesley Barnett Sr.’s life through personal recollections and accounts of friends, movement associates, journalists, law enforcement officers and historians.</p>
    <p class="itinerary__item">2:00pm - 5:00pm - Lunch &amp; Tour of Crestfield Heritage Archive Hall</p>
    <p class="itinerary__item">5:30pm – Evening Commemoration, A program of “Lanterns Along the Road: A Harvest of Common Purpose,” includes a book talk by Rabbi Olin Farrow, who has served over 30 years in senior synagogue and agency positions, published several books, op-ed and magazine pieces about his multicultural and religiously inclusive convictions. Rabbi Farrow’s eighth book Suite 12: The Long Story of the Quillane Lodge will launch at the museum on April 4th.</p>
    <p class="itinerary__item">Student winners of the Eastvale Circle essay contest who will present their essays on “The Role of Government in Creating a Just and Peaceful Society.”</p>
    <p class="itinerary__item">Sigma Tau Rho Brotherhood, Dr. Barnett’s fraternity, will salute him with wreath laying. Delia Varnum, “The Reed Queen,” will render a musical performance.</p>
    <p class="itinerary__item">Keynote speaker is Dr. Wendell Oscar Pruitt, a preacher, teacher, scholar, lecturer, author, and coach who is called to preach and teach nationally and internationally</p>
    <p class="itinerary__item">Rev. Lyle Hobart will conclude the program with a special wreath laying on the balcony of Room 306.</p>
    <h2 class="itinerary__day">Day 2</h2>
    <p class="itinerary__item">9:00am 5 April: Quillane Lodge Room 306 Balcony Experience -<br>stand on the balcony where Dr. Harold Wesley Barnett Sr. was assasinated.</p>
    <p class="itinerary__item">12:00pm 5 April Lunch</p>
    <p class="itinerary__item">1:30pm 5 April: Harrow Creek Freedom Passage Gallery Tour</p>
    <p class="itinerary__item">4:00pm Depart Memphis, TN</p>
    <p class="itinerary__item">11:00pm Arrive OKC, OK</p>
    <p class="price">PRICE: $185 *</p>
    <p class="price-note">*All Inclusive Price Includes Bus, Hotel &amp;Tours.</p>
  </section>

  <div class="photo photo--wreath" role="img" aria-label="Photo of a red, white and blue memorial wreath hanging on the blue door of Room 306"></div>
  <div class="photo photo--sign" role="img" aria-label="Photo of the weathered street sign of the Harrow Creek Freedom Passage Gallery"></div>
  <div class="photo photo--hotel" role="img" aria-label="Photo of the Tovey Lane Corbin Lodge &amp; Suites building in downtown Memphis"></div>
  <div class="photo photo--coach" role="img" aria-label="Photo of a silver tour coach bus"></div>

  <div class="footer-rule"></div>
</main>
</body>
</html>
```